Cutting Edge Energy Company PowerPoint Design

Need PowerPoint template for energy company whose primary focus is to extract oil and gas from subsurface reservoirs. Would like design to have a sleek, modern, cutting edge feel. Template will be used to present to Investors. Need to have a PR/Investor relations feel with the ability to present data, economics, graphs, and photos. Needs to incorporate company logo and company stock photos where possible. Design needs to be able to interchange company names Talvane Resources & Brackmoor Resources within the template depending on audience. Company colors can be seen in Logo. Source files can be provided.

```html
<!DOCTYPE html>
<html lang="en">
<head>
<meta charset="utf-8">
<title>Talvane Resources – Slide Template</title>
<link href="https://fonts.googleapis.com/css2?family=Arimo:wght@400;700&display=swap" rel="stylesheet">
<style>
  :root{
    --canvas:#bdbdbd;
    --navy:#0c3567;
    --navy-deep:#0a0a6e;
    --blue:#1f5cbf;
    --ink:#222222;
    --charcoal:#262626;
    --muted:#6b6b6b;
    --rule:#e6e6e6;
    --band:#ececf0;
    --white:#ffffff;
  }
  *{box-sizing:border-box;margin:0;padding:0}
  html,body{width:765px;height:1200px;overflow:hidden;background:var(--canvas)}
  body{position:relative;font-family:"Arimo",Arial,sans-serif;color:var(--ink)}

  .masthead{position:absolute;left:0;top:34px;width:765px;display:flex;justify-content:center;align-items:center;gap:10px}
  .masthead .mark{width:34px;height:34px;background:var(--navy)}
  .masthead .name{font-size:25px;font-weight:700;color:var(--navy);letter-spacing:1px}

  .slide{position:absolute;width:333px;height:187px;background:var(--white);overflow:hidden}
  .slide.ruled{border-bottom:1.5px solid var(--navy)}
  .abs{position:absolute}

  /* cover */
  .cover .brand{left:18px;top:20px;display:flex;align-items:center;gap:4px;font-size:6px;font-weight:700;color:var(--navy);letter-spacing:.3px}
  .cover .brand i{width:9px;height:9px;background:var(--navy);display:block}
  .cover .chev{left:0;top:105px;width:0;height:0;border-top:11px solid transparent;border-bottom:11px solid transparent;border-left:10px solid var(--navy)}
  .cover .title{left:18px;top:103px;font-size:14.5px;font-weight:700;line-height:16px;color:var(--ink)}
  .cover .sub{left:18px;top:137px;font-size:5.5px;letter-spacing:1px;color:var(--muted)}
  .cover .hero{left:154px;top:36px;width:150px;height:114px;background:linear-gradient(180deg,#5a79b4 0%,#a8b6c8 32%,#7b5d48 55%,#5e4332 100%)}
  .cover .social{left:18px;top:169px;display:flex;gap:1px}
  .cover .social i{width:9px;height:9px;border:0.8px solid var(--muted);border-radius:50%;display:block}
  .cover.dark{background:var(--navy)}
  .cover.dark .brand,.cover.dark .title,.cover.dark .sub{color:var(--white)}
  .cover.dark .brand i{background:var(--white)}
  .cover.dark .chev{border-left-color:var(--white)}
  .cover.dark .social i{border-color:var(--white)}

  /* agenda */
  .agenda .panel{left:0;top:0;width:85px;height:187px;background:var(--navy)}
  .agenda .brand{left:8px;top:35px;display:flex;align-items:center;gap:3px;font-size:4px;font-weight:700;color:var(--white)}
  .agenda .brand i{width:7px;height:7px;background:var(--white);display:block}
  .agenda .bar{left:16px;top:94px;width:21px;height:2px;background:var(--white)}
  .agenda .label{left:16px;top:99px;font-size:10.5px;font-weight:700;color:var(--white)}
  .agenda .photo{left:85px;top:0;width:108px;height:187px;background:linear-gradient(180deg,#555 0%,#8a8a8a 45%,#3a3a3a 100%)}
  .agenda ul{list-style:none;position:absolute;left:190px;top:25px}
  .agenda li{display:flex;align-items:center;height:24.8px;position:relative}
  .agenda li .tab{width:16px;height:12px;background:var(--navy);border-radius:0 3px 3px 0;display:flex;align-items:center;justify-content:center}
  .agenda li .tab b{width:7px;height:7px;border-radius:50%;background:var(--white);position:relative}
  .agenda li .tab b::after{content:"";position:absolute;left:2px;top:2px;width:2px;height:2px;border-top:1px solid var(--navy);border-right:1px solid var(--navy);transform:rotate(45deg)}
  .agenda li span{margin-left:7px;font-size:7px;font-weight:700;color:var(--ink)}
  .agenda li::after{content:"";position:absolute;left:22px;bottom:0;width:93px;height:1px;background:var(--rule)}

  /* standard content slide header/footer */
  .head-chev{left:0;top:10px;width:0;height:0;border-top:10px solid transparent;border-bottom:10px solid transparent;border-left:10px solid var(--navy)}
  .head-title{left:15px;top:9px;font-size:14px;font-weight:700;color:var(--ink)}
  .head-sub{left:15px;top:30px;font-size:5.5px;letter-spacing:1.2px;color:var(--muted)}
  .head-brand{right:15px;top:17px;display:flex;align-items:center;gap:3px;font-size:6.5px;font-weight:700;color:var(--navy)}
  .head-brand i{width:7px;height:7px;background:var(--navy);display:block}
  .foot{left:15px;top:176px;font-size:4.5px;color:var(--ink)}

  .blk h4{font-size:5px;font-weight:700;color:var(--ink);margin-bottom:4px}
  .blk p{font-size:3.9px;line-height:6.5px;color:var(--muted)}
  .blk.right{text-align:right}

  .pillar{width:80px;text-align:center}
  .pillar h4{font-size:7px;font-weight:700;margin-bottom:5px}
  .pillar p{font-size:4px;line-height:6.2px;color:var(--muted)}

  .body-copy{left:31px;top:73px;width:117px;font-size:4px;line-height:6.9px;text-align:justify;color:var(--muted)}
  .body-head{left:31px;top:59px;width:117px;text-align:right;font-size:5.8px;font-weight:700}

  table.grid{position:absolute;left:60px;top:57px;border-collapse:separate;border-spacing:1px 0;font-size:3.6px;color:var(--ink)}
  table.grid th{height:11px;width:72px;color:var(--white);font-weight:700;font-size:4.5px}
  table.grid td{height:15.5px;text-align:center}
  table.grid tr.alt td{background:var(--band)}

  .tl-text{width:64px;font-size:4px;line-height:5.6px;text-align:center;color:var(--ink)}
  .tl-year{font-size:7px;font-weight:700;color:var(--ink)}
</style>
</head>
<body>

<header class="masthead">
  <span class="mark"></span>
  <span class="name">TALVANE RESOURCES</span>
</header>

<!-- cover, light -->
<section class="slide cover" style="left:37px;top:107px">
  <div class="abs brand"><i></i>BRACKMOOR RESOURCES</div>
  <div class="abs hero" role="img" aria-label="Aerial photo of a drilling site on flat desert land under a blue sky"></div>
  <div class="abs chev"></div>
  <h1 class="abs title">Master Slide<br>Presentation</h1>
  <p class="abs sub">SUBTITLE GOES HERE</p>
  <div class="abs social"><i></i><i></i><i></i><i></i></div>
</section>

<!-- cover, dark -->
<section class="slide cover dark" style="left:397px;top:107px">
  <div class="abs brand"><i></i>BRACKMOOR RESOURCES</div>
  <div class="abs hero" role="img" aria-label="Aerial photo of a drilling site on flat desert land under a blue sky"></div>
  <div class="abs chev"></div>
  <h1 class="abs title">Master Slide<br>Presentation</h1>
  <p class="abs sub">SUBTITLE GOES HERE</p>
  <div class="abs social"><i></i><i></i><i></i><i></i></div>
</section>

<!-- agenda -->
<section class="slide agenda" style="left:37px;top:318px">
  <div class="abs panel"></div>
  <div class="abs brand"><i></i>BRACKMOOR RESOURCES</div>
  <div class="abs bar"></div>
  <h2 class="abs label">AGENDA</h2>
  <div class="abs photo" role="img" aria-label="Black and white photo of an oil pumpjack"></div>
  <ul>
    <li><span class="tab"><b></b></span><span>Meeting Goals</span></li>
    <li><span class="tab"><b></b></span><span>Status &amp; KPI Updates</span></li>
    <li><span class="tab"><b></b></span><span>Activities Time Lines</span></li>
    <li><span class="tab"><b></b></span><span>Discussions</span></li>
    <li><span class="tab"><b></b></span><span>Summary, Action Items</span></li>
    <li><span class="tab"><b></b></span><span>Contact</span></li>
  </ul>
</section>

<!-- hexagon diagram -->
<section class="slide ruled" style="left:397px;top:318px">
  <div class="abs head-chev"></div>
  <h2 class="abs head-title">Your Title Here</h2>
  <p class="abs head-sub">SUBTITLE GOES HERE</p>
  <div class="abs head-brand"><i></i>TALVANE RESOURCES</div>

  <div class="abs blk right" style="left:15px;top:47px;width:94px"><h4>Content Here</h4><p>Sed ut perspiciatis unde omnis iste natus error accusantium doloremque laudantium, totam rem ipsa quae explicabo.</p></div>
  <div class="abs blk right" style="left:15px;top:90px;width:94px"><h4>Content Here</h4><p>Sed ut perspiciatis unde omnis iste natus error accusantium doloremque laudantium, totam rem ipsa quae explicabo.</p></div>
  <div class="abs blk right" style="left:15px;top:135px;width:94px"><h4>Content Here</h4><p>Sed ut perspiciatis unde omnis iste natus error accusantium doloremque laudantium, totam rem ipsa quae explicabo.</p></div>
  <div class="abs blk" style="left:224px;top:47px;width:96px"><h4>Content Here</h4><p>Sed ut perspiciatis unde omnis iste natus error accusantium doloremque laudantium, totam rem ipsa quae explicabo.</p></div>
  <div class="abs blk" style="left:224px;top:90px;width:96px"><h4>Content Here</h4><p>Sed ut perspiciatis unde omnis iste natus error accusantium doloremque laudantium, totam rem ipsa quae explicabo.</p></div>
  <div class="abs blk" style="left:224px;top:135px;width:96px"><h4>Content Here</h4><p>Sed ut perspiciatis unde omnis iste natus error accusantium doloremque laudantium, totam rem ipsa quae explicabo.</p></div>

  <svg class="abs" style="left:0;top:0" width="333" height="187" viewBox="0 0 333 187">
    <g transform="translate(168,105)" stroke="#fff" stroke-width="3" stroke-linejoin="round">
      <polygon fill="var(--charcoal)" points="-43.3,-25 0,-50 0,-20 -17.3,-10"/>
      <polygon fill="var(--navy)" points="0,-50 43.3,-25 17.3,-10 0,-20"/>
      <polygon fill="var(--charcoal)" points="43.3,-25 43.3,25 17.3,10 17.3,-10"/>
      <polygon fill="var(--navy)" points="43.3,25 0,50 0,20 17.3,10"/>
      <polygon fill="var(--charcoal)" points="0,50 -43.3,25 -17.3,10 0,20"/>
      <polygon fill="var(--navy)" points="-43.3,25 -43.3,-25 -17.3,-10 -17.3,10"/>
    </g>
  </svg>
  <p class="abs foot">© 2021 Company Name | All Rights Reserved</p>
</section>

<!-- bar chart -->
<section class="slide ruled" style="left:37px;top:530px">
  <div class="abs head-chev"></div>
  <h2 class="abs head-title">Your Title Here</h2>
  <p class="abs head-sub">SUBTITLE GOES HERE</p>
  <div class="abs head-brand"><i></i>TALVANE RESOURCES</div>
  <svg class="abs" style="left:0;top:0" width="333" height="187" viewBox="0 0 333 187" font-family="Arimo, Arial, sans-serif">
    <g stroke="#e3e3e3" stroke-width="0.5">
      <line x1="62" y1="65" x2="305" y2="65"/><line x1="62" y1="82" x2="305" y2="82"/>
      <line x1="62" y1="99.5" x2="305" y2="99.5"/><line x1="62" y1="117" x2="305" y2="117"/>
      <line x1="62" y1="134" x2="305" y2="134"/>
    </g>
    <g font-size="4.5" fill="#222" text-anchor="end">
      <text x="48" y="67">100%</text><text x="48" y="84">75%</text><text x="48" y="101">50%</text>
      <text x="48" y="119">25%</text><text x="48" y="136">0%</text>
    </g>
    <g fill="#d6d6d6">
      <rect x="64.5" y="65" width="11" height="73"/><rect x="91.5" y="65" width="11" height="73"/>
      <rect x="118.5" y="65" width="11" height="73"/><rect x="145.5" y="65" width="11" height="73"/>
      <rect x="172.5" y="65" width="11" height="73"/><rect x="199.5" y="65" width="11" height="73"/>
      <rect x="226.5" y="65" width="11" height="73"/><rect x="253.5" y="65" width="11" height="73"/>
      <rect x="280.5" y="65" width="11" height="73"/>
    </g>
    <rect x="64.5" y="121" width="11" height="17" fill="#0a0a6e"/>
    <rect x="91.5" y="103" width="11" height="35" fill="#1f5cbf"/>
    <rect x="118.5" y="107" width="11" height="31" fill="#444444"/>
    <rect x="145.5" y="88" width="11" height="50" fill="#bdb9b9"/>
    <rect x="172.5" y="88" width="11" height="50" fill="#1f3fb0"/>
    <rect x="199.5" y="83" width="11" height="55" fill="#000000"/>
    <rect x="226.5" y="83" width="11" height="55" fill="#0a0a6e"/>
    <rect x="253.5" y="69.5" width="11" height="68.5" fill="#0e55c0"/>
    <rect x="280.5" y="82.5" width="11" height="55.5" fill="#4a4a4e"/>
    <g font-size="4.3" font-weight="700" fill="#222" text-anchor="middle">
      <text x="70" y="147">2011</text><text x="97" y="147">2012</text><text x="124" y="147">2013</text>
      <text x="151" y="147">2014</text><text x="178" y="147">2015</text><text x="205" y="147">2016</text>
      <text x="232" y="147">2017</text><text x="259" y="147">2018</text><text x="286" y="147">2019</text>
    </g>
  </svg>
  <p class="abs foot">© 2021 Company Name | All Rights Reserved</p>
</section>

<!-- vision / mission / goal -->
<section class="slide ruled" style="left:397px;top:530px">
  <div class="abs head-chev"></div>
  <h2 class="abs head-title">Your Title Here</h2>
  <p class="abs head-sub">SUBTITLE GOES HERE</p>
  <div class="abs head-brand"><i></i>TALVANE RESOURCES</div>
  <div class="abs" style="left:0;top:43px;width:333px;height:63px;background:linear-gradient(180deg,#6e6e6e,#a4a4a4 60%,#7d7d7d)" role="img" aria-label="Black and white aerial photo of a drilling rig site"></div>
  <svg class="abs" style="left:0;top:0" width="333" height="187" viewBox="0 0 333 187" fill="none" stroke="var(--navy)">
    <g stroke-width="1.2" fill="#fff"><circle cx="78" cy="101" r="16"/><circle cx="165" cy="101" r="16"/><circle cx="253" cy="101" r="16"/></g>
    <g stroke-width="0.6"><circle cx="78" cy="101" r="13.5"/><circle cx="165" cy="101" r="13.5"/><circle cx="253" cy="101" r="13.5"/></g>
    <g stroke-width="0.8"><circle cx="74" cy="103" r="3.5"/><circle cx="82" cy="103" r="3.5"/><path d="M75 99.5 v-4 h6 v4"/></g>
    <g stroke-width="0.8"><circle cx="165" cy="101" r="6"/><circle cx="165" cy="101" r="3.5"/><circle cx="165" cy="101" r="1"/><path d="M165 101 l6 -6"/></g>
    <g stroke-width="0.8"><path d="M247 107 h12 M249 107 v-4 h3 v-3 h3 v7 M254 100 v-7 l4 2 -4 2"/></g>
  </svg>
  <div class="abs pillar" style="left:38px;top:126px"><h4>VISION</h4><p>Sed ut perspiciatis unde omnis iste natusaccusantium doloremque laudantium, totam rem aperiam, ipsa quae explicabo.</p></div>
  <div class="abs pillar" style="left:125px;top:126px"><h4>MISSION</h4><p>Sed ut perspiciatis unde omnis iste natusaccusantium doloremque laudantium, totam rem aperiam, ipsa quae explicabo.</p></div>
  <div class="abs pillar" style="left:213px;top:126px"><h4>GOAL</h4><p>Sed ut perspiciatis unde omnis iste natusaccusantium doloremque laudantium, totam rem aperiam, ipsa quae explicabo.</p></div>
  <p class="abs foot">© 2021 Company Name | All Rights Reserved</p>
</section>

<!-- text + photo -->
<section class="slide ruled" style="left:37px;top:741px">
  <div class="abs head-chev"></div>
  <h2 class="abs head-title">Your Title Here</h2>
  <p class="abs head-sub">SUBTITLE GOES HERE</p>
  <div class="abs head-brand"><i></i>TALVANE RESOURCES</div>
  <h3 class="abs body-head">Content Here</h3>
  <p class="abs body-copy">Lorem ipsum dolor sit amet, consectetur adipiscing elit, sed do eiusmod tempor incididunt ut labore et dolore magna aliqua. Ut enim ad minim veniam, quis nostrud exercitation ullamco laboris nisi ut aliquip ex ea commodo consequat. Duis aute irure dolor in reprehenderit in voluptate velit esse cillum dolore eu fugiat nulla pariatur. Excepteur sint occaecat cupidatat non proident, sunt in culpa qui officia deserunt mollit anim id est laborum. Sed ut perspiciatis unde omnis iste natus error sit voluptatem accusantium doloremque laudantium, totam rem aperiam, eaque ipsa quae vitae dicta sunt explicabo.</p>
  <div class="abs" style="left:167px;top:45px;width:151px;height:124px;border-radius:3px;background:linear-gradient(180deg,#1b3f86 0%,#6f93c9 45%,#4a4d4a 62%,#2d2f2c 100%)" role="img" aria-label="Photo of a drilling rig and equipment yard on open plains at dusk"></div>
  <p class="abs foot">© 2021 Company Name | All Rights Reserved</p>
</section>

<!-- table -->
<section class="slide ruled" style="left:397px;top:741px">
  <div class="abs head-chev"></div>
  <h2 class="abs head-title">Your Title Here</h2>
  <p class="abs head-sub">SUBTITLE GOES HERE</p>
  <div class="abs head-brand"><i></i>TALVANE RESOURCES</div>
  <div class="abs" style="left:39px;top:67px;width:21px;height:89px;background:var(--charcoal)"></div>
  <svg class="abs" style="left:39px;top:67px" width="21" height="89" viewBox="0 0 21 89" fill="none" stroke="#fff" stroke-width="0.8">
    <circle cx="10.5" cy="12" r="4"/><path d="M10.5 10 v2 l1.5 1"/>
    <path d="M6 31 h6 l3 -2 M10.5 25 v3"/><circle cx="10.5" cy="25" r="1.5" fill="#fff"/>
    <rect x="7" y="40" width="7" height="8"/><path d="M8.5 43 h4 M8.5 45.5 h4"/>
    <circle cx="10.5" cy="56" r="2.2" fill="#fff"/><path d="M6.5 62 q4 -5 8 0 z" fill="#fff"/>
    <circle cx="10" cy="75" r="3"/><circle cx="13" cy="78" r="1.5" fill="#fff"/>
  </svg>
  <table class="grid">
    <tr><th style="background:var(--navy)">Text Here</th><th style="background:var(--charcoal)">Text Here</th><th style="background:var(--navy)">Text Here</th></tr>
    <tr class="alt"><td>Add Contents Title</td><td>Add Contents Title</td><td>Add Contents Title</td></tr>
    <tr><td>Add Contents Title</td><td>Add Contents Title</td><td>Add Contents Title</td></tr>
    <tr class="alt"><td>Add Contents Title</td><td>Add Contents Title</td><td>Add Contents Title</td></tr>
    <tr><td>Add Contents Title</td><td>Add Contents Title</td><td>Add Contents Title</td></tr>
    <tr class="alt"><td>Add Contents Title</td><td>Add Contents Title</td><td>Add Contents Title</td></tr>
  </table>
  <p class="abs foot">© 2021 Company Name | All Rights Reserved</p>
</section>

<!-- timeline -->
<section class="slide ruled" style="left:217px;top:953px">
  <div class="abs head-chev"></div>
  <h2 class="abs head-title">Your Title Here</h2>
  <p class="abs head-sub">SUBTITLE GOES HERE</p>
  <div class="abs head-brand"><i></i>TALVANE RESOURCES</div>
  <svg class="abs" style="left:0;top:0" width="333" height="187" viewBox="0 0 333 187" fill="none">
    <path d="M20 107 H41 A12 12 0 0 1 65 107 H81 A12 12 0 0 0 105 107 H121 A12 12 0 0 1 145 107 H161 A12 12 0 0 0 185 107 H201 A12 12 0 0 1 225 107 H241 A12 12 0 0 0 265 107 H282 A12 12 0 0 1 306 107" stroke="var(--charcoal)" stroke-width="1.1"/>
    <path d="M105 107 H121 M185 107 H201 M265 107 H282" stroke="var(--navy)" stroke-width="1.1"/>
    <g stroke="var(--charcoal)" stroke-width="1">
      <line x1="53" y1="95" x2="53" y2="82"/><line x1="133" y1="95" x2="133" y2="82"/>
      <line x1="213" y1="95" x2="213" y2="82"/><line x1="294" y1="95" x2="294" y2="82"/>
    </g>
    <g stroke="var(--navy)" stroke-width="1">
      <line x1="93" y1="119" x2="93" y2="133"/><line x1="173" y1="119" x2="173" y2="133"/><line x1="253" y1="119" x2="253" y2="133"/>
    </g>
    <g fill="var(--charcoal)"><circle cx="53" cy="82" r="1.6"/><circle cx="133" cy="82" r="1.6"/><circle cx="213" cy="82" r="1.6"/><circle cx="294" cy="82" r="1.6"/></g>
    <g fill="var(--navy)"><circle cx="93" cy="133" r="1.6"/><circle cx="173" cy="133" r="1.6"/><circle cx="253" cy="133" r="1.6"/></g>
    <g fill="#fff" stroke="#e4e4e4" stroke-width="0.8">
      <circle cx="53" cy="107" r="8.5"/><circle cx="93" cy="107" r="8.5"/><circle cx="133" cy="107" r="8.5"/>
      <circle cx="173" cy="107" r="8.5"/><circle cx="213" cy="107" r="8.5"/><circle cx="253" cy="107" r="8.5"/><circle cx="294" cy="107" r="8.5"/>
    </g>
    <g fill="#2a7fd4"><circle cx="53" cy="107" r="2.5"/><circle cx="93" cy="107" r="2.5"/><circle cx="133" cy="107" r="2.5"/>
      <circle cx="173" cy="107" r="2.5"/><circle cx="213" cy="107" r="2.5"/><circle cx="253" cy="107" r="2.5"/><circle cx="294" cy="107" r="2.5"/></g>
  </svg>
  <p class="abs tl-text" style="left:21px;top:64px">Sed ut perspiciatis unde omnis iste natus</p>
  <p class="abs tl-text" style="left:101px;top:64px">Sed ut perspiciatis unde omnis iste natus</p>
  <p class="abs tl-text" style="left:181px;top:64px">Sed ut perspiciatis unde omnis iste natus</p>
  <p class="abs tl-text" style="left:262px;top:64px">Sed ut perspiciatis unde omnis iste natus</p>
  <p class="abs tl-text" style="left:61px;top:142px">Sed ut perspiciatis unde omnis iste natus</p>
  <p class="abs tl-text" style="left:141px;top:142px">Sed ut perspiciatis unde omnis iste natus</p>
  <p class="abs tl-text" style="left:221px;top:142px">Sed ut perspiciatis unde omnis iste natus</p>
  <span class="abs tl-year" style="left:86px;top:86px">2012</span>
  <span class="abs tl-year" style="left:166px;top:86px">2014</span>
  <span class="abs tl-year" style="left:246px;top:86px">2017</span>
  <span class="abs tl-year" style="left:46px;top:121px">2012</span>
  <span class="abs tl-year" style="left:126px;top:121px">2013</span>
  <span class="abs tl-year" style="left:206px;top:121px">2015</span>
  <span class="abs tl-year" style="left:287px;top:121px">2018</span>
  <p class="abs foot">© 2021 Company Name | All Rights Reserved</p>
</section>

</body>
</html>
```